Pella Acupuncture Business Card Design

I would like a business card design for my acupuncture business which is based from 2 practices in Melbourne, Australia.

The front of the card should include:

*The Logo
* Name - Miranda Tovelisca (B.App.Sc.(TCM), Dip.Rem.Mass.). (I would like the letters after my name in slightly smaller font)
* Mobile number - 0472 318 604
* Web address - www.pellaacupuncture-example.com.au

On the back of the card I would somehow like to fit my 2 clinic addresses in. They are:

The Birchwood Restoration Rooms
842 Fennimore Rd, Camberwell VIC 3124
Ph: 1300 274 518

Quillbrook Integrative & Eastern Herbal Therapy Clinic
31 Marlowby Rd, Malvern East VIC 3145
Ph: (03) 9871 3352

If there is space, I'd also like to add to the back of the card - Next Appointment............................ (or something along those lines).

Thanks and happy designing!

Target Market(s)

Health consumers, and colleagues in the health industry

Industry/Entity Type

Clinic

Contact Information for Business Card

as above in brief

Requirements
Must have
• I've seen some ok designs coming in, however I'd like to avoid the generic look with the added curved line details etc. I don't particularly need extra patterns added to the card. I'd prefer it to look quite clean and simple, and using more earthy colours (I'm not super keen on the lime green that a lot of designs seem to include. I don't mind the full black or white look, (obviously the back side needs to be a lighter colour to allow me to write appointment details on it). I also quite like the idea of the background looking like brown recycled paper (just an idea - that's not 100% necessary).
Nice to have
• I have an idea that I could have the main flower part of the logo printed as metallic.
Should not have
• Generic patterns and too much added detail.

```html
<!DOCTYPE html>
<html lang="en">
<head>
<meta charset="utf-8">
<title>Pella Acupuncture – Business Card</title>
<link rel="stylesheet" href="https://fonts.googleapis.com/css2?family=Noto+Sans:wght@400;700&display=swap">
<style>
  :root {
    --page: #ffffff;
    --front-dark: #1f1a15;
    --front-mid: #2e251d;
    --bronze: #b8925a;
    --bronze-light: #d9bd88;
    --kraft: #e4d2b2;
    --kraft-light: #efe3cc;
    --earth-ink: #3a2c1f;
    --light-ink: #f4ead8;
    --mark-disc: #b8925a;
    --mark-text: #1f1a15;
  }
  * { margin: 0; padding: 0; box-sizing: border-box; }
  html, body {
    width: 1057px; height: 1200px; overflow: hidden;
    background: var(--page);
    font-family: "Noto Sans", sans-serif;
  }
  .sheet { position: relative; width: 1057px; height: 1200px; }
  .card {
    position: absolute; left: 24px; width: 1008px; height: 562px; overflow: hidden;
  }
  .card--front {
    top: 24px;
    background:
      radial-gradient(ellipse 45% 55% at 50% 45%, rgba(184,146,90,.22) 0%, rgba(184,146,90,0) 100%),
      linear-gradient(180deg, var(--front-mid) 0%, var(--front-dark) 100%);
  }
  .card--back {
    top: 615px;
    background:
      radial-gradient(ellipse 45% 50% at 50% 42%, var(--kraft-light) 0%, rgba(239,227,204,0) 100%),
      linear-gradient(180deg, var(--kraft) 0%, #dcc7a3 100%);
  }
  .front__rule {
    position: absolute; left: 0; top: 432px; width: 100%; height: 2px;
    background: linear-gradient(90deg, rgba(217,189,136,0) 0%, rgba(217,189,136,.9) 30%, rgba(217,189,136,.9) 70%, rgba(217,189,136,0) 100%);
  }
  .brand-mark {
    position: absolute; left: 337px; top: 115px; width: 334px; height: 334px;
    border-radius: 50%;
    background: radial-gradient(circle at 40% 35%, var(--bronze-light) 0%, var(--mark-disc) 70%);
    display: flex; align-items: center; justify-content: center; text-align: center;
  }
  .brand-mark__name {
    color: var(--mark-text); font-size: 34px; font-weight: 400; line-height: 1.2;
  }
  .practitioner { position: absolute; left: 40px; top: 446px; color: var(--light-ink); }
  .practitioner__name { font-size: 33px; font-weight: 700; line-height: 1.2; }
  .practitioner__quals { font-size: 22px; font-weight: 400; letter-spacing: -0.3px; margin-top: 2px; }
  .contact {
    position: absolute; right: 40px; top: 448px; text-align: right; color: var(--light-ink);
    font-weight: 400;
  }
  .contact__mobile { font-size: 31px; line-height: 1.2; }
  .contact__web { font-size: 25px; margin-top: 4px; letter-spacing: -0.3px; }
  .clinics { position: absolute; left: 46px; top: 84px; color: var(--earth-ink); }
  .clinic { font-size: 30px; line-height: 39px; font-weight: 400; font-style: normal; }
  .clinic + .clinic { margin-top: 14px; }
  .appointment {
    position: absolute; left: 46px; top: 480px; color: var(--earth-ink); font-size: 26px;
  }
</style>
</head>
<body>
<main class="sheet">
  <section class="card card--front">
    <div class="front__rule"></div>
    <div class="brand-mark">
      <span class="brand-mark__name">Pella<br>Acupuncture</span>
    </div>
    <div class="practitioner">
      <p class="practitioner__name">Miranda Tovelisca</p>
      <p class="practitioner__quals">(B.App.Sc.(TCM), Dip.Rem.Mass.)</p>
    </div>
    <div class="contact">
      <p class="contact__mobile">0472 - 318 604</p>
      <p class="contact__web">www.pellaacupuncture-example.com.au</p>
    </div>
  </section>

  <section class="card card--back">
    <div class="clinics">
      <address class="clinic">
        The Birchwood Restoration Rooms<br>
        842 Fennimore Rd, Camberwell VIC 3124<br>
        Ph: 1300 274 518
      </address>
      <address class="clinic">
        Quillbrook Integrative &amp; Eastern Herbal Therapy Clinic<br>
        31 Marlowby Rd, Malvern East VIC 3145<br>
        Ph: (03) 9871 3352
      </address>
    </div>
    <p class="appointment">Next Appointment...........................</p>
  </section>
</main>
</body>
</html>
```